Cedarbend Ridge Footraces

We need a website (wordpress) design for a new website that we will be launching. This is for a new trail racing series in Canada.
We recently had a logo designed so want to incorporate the colours of the logo on the website design. Especially the dark blue, green and orange.
Websites that we like for comparison of trail running race themes are:
https://www.mossyboulderrunning.example/
https://www.quillpathcircuit.example/
http://www.tidecovecircuit.example/
https://www.amberfellcircuit.example/
http://www.brookmarchrunseries.example/

Target Market(s)

Outdoor trail runners

Coding

Coded - Design and coding required

Number of Pages Required

4 page

Font styles to use
Sans Serif

Colors
0255a3
33b8a4
f37122

Requirements
Must have
• There will be a main page with eye catching design noting what we do. Page 2 and 3 will be for each race in the series. Page 1 will be a specific race, and page 2 with be for another race. page 3 and 4 will be for future races that we add so that each race has their own page.
• Our races all take place in the mountains, so using graphics including mountains, rivers, trees is all a requirement for us.
• Our logo is attached, we want to use the colours of the logo in the website design.
Nice to have
• Outdoor theme is a nice to have. We like wood and earth tone colours, and pictures/graphics of runners and mountains and trees.
• There are 4 people involved in our organization. We'd like a photo and brief blurb of each of us, similar to how this website did their layout: https://www.mossyboulderrunning.example/

```html
<!DOCTYPE html>
<html lang="en">
<head>
<meta charset="utf-8">
<title>Cedarbend Ridge Footraces</title>
<link href="https://fonts.googleapis.com/css2?family=Montserrat:wght@400;600;700;800&family=Open+Sans:wght@400;600;700&display=swap" rel="stylesheet">
<style>
:root{
  --blue:#0255a3;
  --green:#33b8a4;
  --orange:#f37122;
  --ink:#1f2a36;
  --text:#6b7480;
  --light:#f3f4f6;
  --line:#e3e6ea;
  --footer:#1c1d20;
  --footer-bottom:#141517;
  --white:#ffffff;
}
*{box-sizing:border-box;margin:0;padding:0}
html,body{width:1200px;height:3024px;overflow:hidden}
body{font-family:"Open Sans",Arial,sans-serif;color:var(--text);background:var(--white);position:relative;font-size:13px;line-height:1.6}
h1,h2,h3,h4,.nav a,.btn{font-family:"Montserrat",Arial,sans-serif}
.btn{display:inline-block;font-size:12px;font-weight:600;padding:11px 26px;text-decoration:none}
.btn-orange{background:var(--orange);color:var(--white)}
.btn-outline{border:2px solid var(--white);color:var(--white)}
.link-more{font-family:"Montserrat",Arial,sans-serif;font-size:12px;font-weight:700;color:var(--ink);text-decoration:none;border-bottom:2px solid var(--orange);padding-bottom:2px}

/* Header + hero */
.hero{position:absolute;left:0;top:0;width:1200px;height:700px;overflow:hidden}
.hero-photo{position:absolute;inset:0;background:linear-gradient(180deg,#8fb9dc 0%,#b9d3e6 30%,#7a9a8a 55%,#4f7b47 75%,#3b6236 100%)}
.hero-shade{position:absolute;inset:0;background:linear-gradient(90deg,rgba(10,30,60,.45) 0%,rgba(10,30,60,.1) 60%,rgba(0,0,0,0) 100%)}
.site-header{position:absolute;left:0;top:0;width:1200px;height:90px;display:flex;align-items:center;padding:0 40px;background:rgba(2,40,80,.25)}
.brand{display:flex;align-items:center;gap:10px;width:250px}
.brand-mark{width:34px;height:34px;border-radius:50%;background:var(--orange)}
.brand-name{font-family:"Montserrat",Arial,sans-serif;font-weight:700;font-size:13px;color:var(--white);line-height:1.2;width:110px}
.nav{display:flex;gap:34px;margin-left:40px}
.nav a{color:var(--white);font-size:12px;font-weight:600;text-decoration:none}
.call-box{position:absolute;right:160px;top:0;width:130px;height:90px;background:var(--blue);display:flex;align-items:center;gap:10px;padding-left:18px;color:var(--white)}
.call-box small{display:block;font-size:10px;font-weight:700;line-height:1.2}
.call-box span{font-size:11px}
.hero-content{position:absolute;left:160px;top:270px;width:760px}
.hero-content h1{font-size:68px;font-weight:800;color:var(--white);line-height:1;letter-spacing:-1px;white-space:nowrap}
.hero-content p{color:var(--white);font-size:12px;margin:22px 0 34px;width:470px}
.hero-content .btn{margin-right:14px}
.slide-arrow{position:absolute;top:345px;width:32px;height:32px;background:rgba(255,255,255,.85);display:flex;align-items:center;justify-content:center}
.slide-arrow.prev{left:40px}
.slide-arrow.next{right:40px}

/* Race series */
.series{position:absolute;left:0;top:700px;width:1200px;height:620px;background:var(--light)}
.race-card{position:absolute;width:210px;background:var(--white);box-shadow:0 6px 18px rgba(0,0,0,.08)}
.race-photo{height:130px;background:linear-gradient(160deg,#9cc0d8,#6f9a68 60%,#4d6f42)}
.race-caption{height:90px;padding:14px 16px 0;border-top:3px solid var(--orange)}
.race-caption h4{font-size:10px;font-weight:700;color:var(--blue);text-transform:uppercase;margin-bottom:6px}
.race-caption p{font-size:10px;line-height:1.5}
.series-panel{position:absolute;left:610px;top:100px;width:430px;background:var(--white);box-shadow:0 8px 24px rgba(0,0,0,.08);padding:44px 40px 40px}
.series-panel h2{font-size:25px;font-weight:800;color:var(--ink);line-height:1.2;text-align:center;margin-bottom:24px}
.series-panel h2::before{content:"";display:block;width:4px;height:26px;background:var(--orange);margin:0 auto 14px}
.details{width:100%;border-collapse:collapse;font-size:11px}
.details th{text-align:left;color:var(--ink);font-weight:700;width:110px;padding:7px 0;border-bottom:1px solid var(--line);vertical-align:top}
.details td{padding:7px 0;border-bottom:1px solid var(--line)}
.series-panel .btn{display:block;width:200px;margin:26px auto 0;text-align:center;padding:10px 0;font-size:11px}

/* What we do */
.what-we-do{position:absolute;left:0;top:1320px;width:1200px;height:220px;padding:70px 160px 0}
.what-we-do h2,.team h2{font-size:28px;font-weight:800;color:var(--ink);margin-bottom:10px}
.what-we-do .lead,.team .lead{font-weight:600;color:var(--ink);font-size:12px;width:300px;margin-bottom:16px}
.what-we-do .body{position:absolute;left:620px;top:70px;width:420px;font-size:12px}

/* Results */
.results{position:absolute;left:0;top:1540px;width:1200px;height:550px;background:var(--light)}
.results-card{position:absolute;left:160px;top:60px;width:380px;height:430px;background:var(--white);box-shadow:0 8px 24px rgba(0,0,0,.08);padding:40px 40px;text-align:center}
.results-card h2{font-size:26px;font-weight:800;color:var(--ink)}
.results-card h2::before{content:"";display:block;width:4px;height:26px;background:var(--orange);margin:0 auto 12px}
.results-card p{font-size:11px;margin:16px 0 24px}
.badges{display:grid;grid-template-columns:1fr 1fr;gap:18px 0;justify-items:center}
.badge{width:62px;height:62px;border-radius:50%}
.results-photo{position:absolute;left:620px;top:0;width:580px;height:550px;background:linear-gradient(180deg,#a7cbe6 0%,#cfe0ea 30%,#8fa878 55%,#6b8a50 75%,#8d7b56 100%)}

/* Team */
.team{position:absolute;left:0;top:2090px;width:1200px;height:470px;padding:70px 160px 0}
.team .quote{position:absolute;left:620px;top:70px;width:420px;border-left:3px solid var(--blue);padding-left:16px;font-weight:700;color:var(--ink);font-size:14px}
.member{position:absolute;left:160px;top:230px;width:360px}
.member h4{font-size:13px;font-weight:700;color:var(--ink);margin-bottom:8px}
.member h4 span{font-family:"Open Sans",Arial,sans-serif;font-weight:400;font-size:10px;color:var(--text);margin-left:6px}
.member p{font-size:10px;line-height:1.6;margin-bottom:14px}
.member-frame{position:absolute;left:640px;top:200px;width:340px;height:220px;border:4px solid var(--blue)}
.member-photo{position:absolute;left:620px;top:180px;width:280px;height:260px;background:linear-gradient(180deg,#eef1f4,#d4dbe3);box-shadow:0 6px 18px rgba(0,0,0,.08)}
.member-dots{position:absolute;left:995px;top:215px;display:flex;flex-direction:column;gap:8px}
.member-dots i{display:block;width:8px;height:8px;background:var(--blue)}

/* Footer */
.site-footer{position:absolute;left:0;top:2560px;width:1200px;height:410px;background:var(--footer);padding:70px 160px 0;color:#9a9ea5;font-size:11px}
.footer-col{position:absolute;top:70px}
.footer-col h4{font-size:11px;font-weight:700;color:var(--white);margin-bottom:18px;text-transform:uppercase}
.footer-brand{left:160px;width:270px}
.footer-brand h3{font-size:20px;font-weight:700;color:var(--orange);margin-bottom:14px}
.footer-contact{left:480px;width:250px}
.contact-row{display:flex;gap:10px;margin-bottom:12px;line-height:1.5}
.contact-row svg{flex:none;margin-top:2px}
.footer-links{left:790px;width:250px}
.footer-links ul{list-style:none;columns:2;column-gap:30px}
.footer-links li{margin-bottom:8px}
.newsletter{position:absolute;left:160px;top:250px;width:880px}
.newsletter h4{font-size:11px;font-weight:700;color:var(--white);text-transform:uppercase;margin-bottom:6px}
.newsletter p{width:280px}
.news-form{position:absolute;left:320px;top:6px;display:flex}
.news-input{width:440px;height:40px;background:#2a2c30;color:#70747b;font-size:11px;padding:11px 16px}
.news-btn{width:120px;height:40px;background:var(--blue);color:var(--white);font-family:"Montserrat",Arial,sans-serif;font-weight:700;font-size:11px;display:flex;align-items:center;justify-content:center}
.footer-bottom{position:absolute;left:0;top:2970px;width:1200px;height:54px;background:var(--footer-bottom);display:flex;align-items:center;justify-content:space-between;padding:0 160px;color:#7c8087;font-size:10px}
.socials{display:flex;gap:8px}
.socials i{display:block;width:22px;height:22px;border-radius:50%;border:1px solid #7c8087}
</style>
</head>
<body>

<section class="hero">
  <div class="hero-photo" role="img" aria-label="Trail runner with poles on a green mountain ridge under a bright blue sky"></div>
  <div class="hero-shade"></div>
  <header class="site-header">
    <div class="brand"><span class="brand-mark"></span><span class="brand-name">CEDARBEND RIDGE</span></div>
    <nav class="nav">
      <a href="#">Home</a><a href="#">About</a><a href="#">Photos</a><a href="#">Results</a><a href="#">Faqs</a><a href="#">Volunteer</a><a href="#">Budgets</a><a href="#">Blog</a>
    </nav>
    <div class="call-box">
      <svg width="20" height="20" viewBox="0 0 24 24" fill="#fff"><path d="M6.6 10.8a15.1 15.1 0 0 0 6.6 6.6l2.2-2.2c.3-.3.7-.4 1-.2 1.1.4 2.3.6 3.6.6.6 0 1 .4 1 1V20c0 .6-.4 1-1 1A17 17 0 0 1 3 4c0-.6.4-1 1-1h3.5c.6 0 1 .4 1 1 0 1.3.2 2.5.6 3.6.1.3 0 .7-.2 1z"/></svg>
      <div><small>CALL</small><span>+1 555 0142</span></div>
    </div>
  </header>
  <div class="slide-arrow prev"><svg width="10" height="12" viewBox="0 0 10 12"><path d="M8 1 2 6l6 5" stroke="#1f2a36" stroke-width="2" fill="none"/></svg></div>
  <div class="slide-arrow next"><svg width="10" height="12" viewBox="0 0 10 12"><path d="m2 1 6 5-6 5" stroke="#1f2a36" stroke-width="2" fill="none"/></svg></div>
  <div class="hero-content">
    <h1>Cedarbend Ridge</h1>
    <p>Lorem Ipsum is simply dummy text of the printing and typesetting industry. Lorem Ipsum has been the industry's standard dummy text ever since the 1500s, when an unknown printer took a galley.</p>
    <a class="btn btn-outline" href="#">Learn More</a><a class="btn btn-orange" href="#">Contact Us</a>
  </div>
</section>

<section class="series">
  <article class="race-card" style="left:160px;top:100px">
    <div class="race-photo" role="img" aria-label="Runners on a rocky mountain trail"></div>
    <div class="race-caption"><h4>Granite Hollow Trail Race</h4><p>Lorem Ipsum is simply dummy text of the printing.</p></div>
  </article>
  <article class="race-card" style="left:380px;top:80px">
    <div class="race-photo" role="img" aria-label="Trail runner crossing a forest river"></div>
    <div class="race-caption"><h4>Birchwind Summit Race</h4><p>Lorem Ipsum is simply dummy text of the printing.</p></div>
  </article>
  <article class="race-card" style="left:160px;top:340px">
    <div class="race-photo" role="img" aria-label="Group of runners in a mountain valley"></div>
    <div class="race-caption"><h4>Fernbrook Valley Run</h4><p>Lorem Ipsum is simply dummy text of the printing.</p></div>
  </article>
  <article class="race-card" style="left:380px;top:320px">
    <div class="race-photo" role="img" aria-label="Runner on a ridge among pine trees"></div>
    <div class="race-caption"><h4>Larkspur Crest Race</h4><p>Lorem Ipsum is simply dummy text of the printing.</p></div>
  </article>
  <div class="series-panel">
    <h2>Cedarbend Ultra &amp; Trail Race Series</h2>
    <table class="details">
      <tr><th>Date</th><td>January 3, 2019</td></tr>
      <tr><th>Time</th><td>9am–2pm &amp; 4pm–9pm</td></tr>
      <tr><th>Location</th><td>Fern Lake &amp; Ash Hollow</td></tr>
      <tr><th>Distances</th><td>5 km, 10 km, 21 km</td></tr>
      <tr><th>Description</th><td>This race is based on a professional adventure. The sports all over the world are welcome.</td></tr>
    </table>
    <a class="btn btn-orange" href="#">View More Race Series</a>
  </div>
</section>

<section class="what-we-do">
  <h2>What We Do</h2>
  <p class="lead">Lorem Ipsum is simply dummy text here</p>
  <a class="link-more" href="#">Learn More</a>
  <p class="body">Lorem Ipsum is simply dummy text of the printing and typesetting industry. Lorem Ipsum has been the industry's standard dummy text ever since the 1500s, when an unknown printer took a galley of type and scrambled it to make a type specimen book. It has survived not only five centuries, but also the leap into electronic typesetting, remaining essentially unchanged.</p>
</section>

<section class="results">
  <div class="results-card">
    <h2>Results</h2>
    <p>Lorem Ipsum is simply dummy text of the printing and typesetting industry. Lorem Ipsum has been the industry's standard dummy text ever since the 1500s, when an unknown printer took a galley of type and scrambled it to make a type specimen book.</p>
    <div class="badges">
      <span class="badge" style="background:#d98a3a"></span>
      <span class="badge" style="background:#6f8f3c"></span>
      <span class="badge" style="background:#2b2b2b"></span>
      <span class="badge" style="background:#9a3a2a"></span>
    </div>
  </div>
  <div class="results-photo" role="img" aria-label="Trail runner on a rocky coastal mountain path"></div>
</section>

<section class="team">
  <h2>Our Team</h2>
  <p class="quote">Lorem Ipsum is simply dummy text of the printing and typesetting industry. Lorem Ipsum is the industry's standard text</p>
  <div class="member">
    <h4>Marlon Hatchley <span>Race Director</span></h4>
    <p>Lorem Ipsum is simply dummy text of the printing and typesetting industry. Lorem Ipsum has been the industry's standard dummy text ever since the 1500s.</p>
    <p>When an unknown printer took a galley of type and scrambled it to make a type specimen book and more.</p>
    <a class="link-more" href="#">Learn More</a>
  </div>
  <div class="member-frame"></div>
  <div class="member-photo" role="img" aria-label="Portrait of a team member"></div>
  <div class="member-dots"><i></i><i></i><i></i></div>
</section>

<footer class="site-footer">
  <div class="footer-col footer-brand">
    <h3>CEDARBEND - RIDGE</h3>
    <p>Lorem Ipsum is simply dummy text of the printing and typesetting industry. Lorem Ipsum has been the standard dummy text ever since the 1500s.</p>
  </div>
  <div class="footer-col footer-contact">
    <h4>Contact Us</h4>
    <div class="contact-row"><svg width="12" height="12" viewBox="0 0 24 24" fill="#9a9ea5"><path d="M6.6 10.8a15.1 15.1 0 0 0 6.6 6.6l2.2-2.2c.3-.3.7-.4 1-.2 1.1.4 2.3.6 3.6.6.6 0 1 .4 1 1V20c0 .6-.4 1-1 1A17 17 0 0 1 3 4c0-.6.4-1 1-1h3.5c.6 0 1 .4 1 1 0 1.3.2 2.5.6 3.6.1.3 0 .7-.2 1z"/></svg><span>+1 555 0142<br>+1 555 0178</span></div>
    <div class="contact-row"><svg width="12" height="12" viewBox="0 0 24 24" fill="#9a9ea5"><path d="M2 5h20v14H2z" opacity=".4"/><path d="m2 5 10 8 10-8" stroke="#9a9ea5" stroke-width="2" fill="none"/></svg><span>hello@cedarbendridge.example</span></div>
    <div class="contact-row"><svg width="12" height="12" viewBox="0 0 24 24" fill="#9a9ea5"><path d="M12 2a7 7 0 0 0-7 7c0 5 7 13 7 13s7-8 7-13a7 7 0 0 0-7-7zm0 9.5a2.5 2.5 0 1 1 0-5 2.5 2.5 0 0 1 0 5z"/></svg><span>214 Pinecrest Lane, Cedarbend</span></div>
  </div>
  <div class="footer-col footer-links">
    <h4>Quick Links</h4>
    <ul><li>Home</li><li>About</li><li>Photos</li><li>Results</li><li>Faqs</li><li>Volunteer</li><li>Budgets</li><li>Blog</li><li>Contact</li><li>Privacy Policy</li></ul>
  </div>
  <div class="newsletter">
    <h4>Get the Newsletter</h4>
    <p>Lorem Ipsum is simply dummy text of the printing industry.</p>
    <div class="news-form"><div class="news-input">Enter your email</div><div class="news-btn">SUBSCRIBE</div></div>
  </div>
</footer>
<div class="footer-bottom">
  <span>© Copyright 2019 Cedarbend Ridge. All Rights Reserved.</span>
  <div class="socials"><i></i><i></i><i></i></div>
</div>

</body>
</html>
```